Business Card Design For Marketing Agnecy LVT

Need business card design for marketing agency.

Dorian Pell
President, CEO
1-555-304-2917
dorian@lumenvaletrewards.net
www.LumenValeTrewards.biz

Back Side:
Boost Sales Using Rewards, Incentives & Giveaways
Get A Free Sample Package

Target Market(s)

B2B

Industry/Entity Type

Marketing

Contact Information for Business Card

Dorian Pell
President, CEO
1-555-304-2917

Back Side:
Get A Free Sample Package

Please note that my current url is OLD DESIGN. I am working on new design and want the business card to match color themes at least on new site. Here is the demo link for new site so you can see the colors I use, etc.

http://pagekilnstudio.example/qx/dorian/lvt_final/index.html

Requirements
Must have
• Please note that my current url is OLD DESIGN. I am working on new design and want the business card to match color themes at least on new site. Here is the demo link for new site so you can see the colors I use, etc.

Nice to have

Should not have

```html
<!DOCTYPE html>
<html lang="en">
<head>
<meta charset="utf-8">
<title>LVT Business Card – Front and Back</title>
<link rel="stylesheet" href="https://fonts.googleapis.com/css2?family=Montserrat:wght@500;700&family=Oswald:wght@600&family=Roboto:wght@400;500&display=swap">
<style>
  :root {
    --backdrop: #e6e6e6;
    --card: #2b2b2b;
    --brand-blue: #1b78c9;
    --text-light: #e9e9e9;
    --text-muted: #bdbdbd;
    --mark-faint: #363636;
    --rule: #8a8a8a;
  }
  * { box-sizing: border-box; margin: 0; padding: 0; }
  html, body { width: 1200px; height: 801px; overflow: hidden; }
  body {
    background: var(--backdrop);
    font-family: "Roboto", Arial, sans-serif;
    display: flex;
    align-items: center;
    justify-content: center;
    gap: 40px;
  }
  .card {
    position: relative;
    width: 540px;
    height: 309px;
    background: var(--card);
    border-bottom: 4px solid var(--brand-blue);
    box-shadow: 0 14px 28px rgba(0,0,0,.25);
    overflow: hidden;
  }

  /* Front */
  .front .brand {
    position: absolute;
    top: 46px;
    left: 60px;
    display: flex;
    align-items: center;
    gap: 14px;
  }
  .brand-dot {
    width: 18px; height: 18px;
    border-radius: 50%;
    background: var(--brand-blue);
  }
  .brand-name {
    font-family: "Montserrat", Arial, sans-serif;
    font-weight: 700;
    font-size: 64px;
    letter-spacing: 4px;
    color: var(--brand-blue);
    line-height: 1;
  }
  .front .identity {
    position: absolute;
    left: 60px;
    bottom: 52px;
  }
  .person-name {
    font-family: "Oswald", Arial, sans-serif;
    font-weight: 600;
    font-size: 30px;
    color: var(--brand-blue);
    text-transform: uppercase;
    line-height: 1.05;
  }
  .person-title {
    font-size: 16px;
    color: var(--text-light);
    margin-top: 4px;
  }
  .divider {
    position: absolute;
    left: 250px;
    bottom: 46px;
    width: 1px;
    height: 80px;
    background: var(--rule);
  }
  .contact-list {
    position: absolute;
    left: 272px;
    bottom: 54px;
    list-style: none;
    font-size: 12.5px;
    color: var(--text-light);
  }
  .contact-list li {
    display: flex;
    align-items: center;
    gap: 8px;
    margin-top: 7px;
  }
  .contact-list svg { width: 12px; height: 12px; flex: none; fill: none; stroke: var(--brand-blue); stroke-width: 1.6; }
  .contact-list .web-link { color: var(--brand-blue); }

  /* Back */
  .back .mark-decoration {
    position: absolute;
    left: -10px;
    bottom: -40px;
    font-family: "Montserrat", Arial, sans-serif;
    font-weight: 700;
    font-size: 190px;
    letter-spacing: 6px;
    color: var(--mark-faint);
    line-height: 1;
  }
  .back .pitch {
    position: absolute;
    right: 34px;
    top: 112px;
    width: 230px;
  }
  .tagline {
    font-size: 17px;
    line-height: 1.3;
    color: var(--text-light);
  }
  .cta {
    font-size: 17px;
    color: var(--brand-blue);
    margin-top: 2px;
  }
  .site {
    font-size: 13px;
    font-weight: 500;
    color: #ffffff;
    margin-top: 20px;
  }
</style>
</head>
<body>

  <section class="card front" aria-label="Card front">
    <div class="brand">
      <span class="brand-dot"></span>
      <span class="brand-name">LVT</span>
    </div>

    <div class="identity">
      <p class="person-name">Dorian Pell</p>
      <p class="person-title">President, CEO</p>
    </div>

    <span class="divider"></span>

    <ul class="contact-list">
      <li>
        <svg viewBox="0 0 12 12"><path d="M2.5 1.5h2l1 2.5-1.3 1a6 6 0 0 0 2.8 2.8l1-1.3 2.5 1v2a1 1 0 0 1-1 1A9 9 0 0 1 1.5 2.5a1 1 0 0 1 1-1z"/></svg>
        1-555-304-2917
      </li>
      <li>
        <svg viewBox="0 0 12 12"><rect x="1" y="2.5" width="10" height="7"/><path d="M1 2.5l5 4 5-4"/></svg>
        dorian@lumenvaletrewards.net
      </li>
      <li>
        <svg viewBox="0 0 12 12"><circle cx="6" cy="6" r="5"/><path d="M1 6h10M6 1c2.5 2.7 2.5 7.3 0 10M6 1c-2.5 2.7-2.5 7.3 0 10"/></svg>
        <span class="web-link">www.LumenValeTrewards.biz</span>
      </li>
    </ul>
  </section>

  <section class="card back" aria-label="Card back">
    <span class="mark-decoration" aria-hidden="true">LVT</span>

    <div class="pitch">
      <p class="tagline">Boost Sales Using Rewards Incentives &amp; Giveaways</p>
      <p class="cta">Get A Free Sample Package</p>
      <p class="site">www.LumenValeTrewards.biz</p>
    </div>
  </section>

</body>
</html>
```